Belford & Company

We are a boutique commercial real estate firm. For our Business card design - sleek, modern, yet high-end/classy. Please see our website: belfordandcompany.example for details.

We currently need 2 business card names and the ability to add/change the business card information -
Name, Title, Address, Office #, Mobile #, Fax, Email and company website.

Industry/Entity Type

Real Estate

Contact Information for Business Card

Business card design - sleek, modern, yet high-end/classy. Please see our website: belfordandcompany.example for details.

Also, we'd like to have our slogan "Careful Work, Lasting Value." somewhere in there. We'd like to make some part of it raised or a different texture if possible.
Color #'s:
blue 19 36 128
light gray 222 222 221
dark gray 107 120 128

Also, we'd like to have our slogan "Careful Work, Lasting Value." somewhere in there. We'd like to make some part of it raised or a different texture if possible - grey on one side and blue on the other - rounded edges preferred. Maybe either metal/silver/grey raised logo on the back. Thank you!!

Requirements
Must have
• Sleek, modern, clean and classy design

```html
<!DOCTYPE html>
<html lang="en">
<head>
<meta charset="utf-8">
<title>Belford &amp; Company – Business Card</title>
<link rel="stylesheet" href="https://fonts.googleapis.com/css2?family=Oswald:wght@500&family=Lato:wght@400&family=Montserrat:wght@600&display=swap">
<style>
  :root {
    --backdrop: #5b5b5b;
    --brand-blue: #1f45a0;
    --ink: #1c1c1c;
    --light-gray: #dededd;
    --dark-gray: #6b7880;
    --paper: #ffffff;
  }
  html, body {
    margin: 0;
    width: 1200px;
    height: 900px;
    overflow: hidden;
    background: var(--backdrop);
  }
  .canvas {
    position: relative;
    width: 1200px;
    height: 900px;
  }
  .card {
    position: absolute;
    top: 200px;
    width: 310px;
    height: 502px;
    box-shadow: 3px 4px 8px rgba(0,0,0,0.45);
    box-sizing: border-box;
  }
  .card-front {
    left: 253px;
    background: var(--paper);
    border-radius: 60px 0 60px 0;
  }
  .card-back {
    left: 627px;
    background: var(--brand-blue);
    border-radius: 0 60px 0 60px;
  }
  .brand {
    position: absolute;
    left: 48px;
    top: 130px;
    display: flex;
    align-items: center;
    gap: 10px;
  }
  .brand-square {
    width: 22px;
    height: 22px;
    background: var(--dark-gray);
    flex: none;
  }
  .brand-name {
    font-family: "Lato", sans-serif;
    font-weight: 400;
    font-size: 21px;
    line-height: 24px;
    color: var(--brand-blue);
    margin: 0;
    white-space: nowrap;
  }
  .person {
    position: absolute;
    left: 33px;
    top: 284px;
  }
  .person-name {
    font-family: "Oswald", sans-serif;
    font-weight: 500;
    font-size: 23px;
    line-height: 26px;
    color: var(--brand-blue);
    text-transform: uppercase;
    margin: 0;
  }
  .person-title {
    font-family: "Lato", sans-serif;
    font-size: 14.5px;
    line-height: 17px;
    color: var(--ink);
    margin: 0;
  }
  .contact-list {
    list-style: none;
    margin: 0;
    padding: 0;
    position: absolute;
    left: 33px;
    top: 334px;
    font-family: "Lato", sans-serif;
    font-size: 14.5px;
    line-height: 17px;
    color: var(--ink);
  }
  .contact-list li {
    display: flex;
    align-items: center;
    gap: 5px;
    white-space: nowrap;
  }
  .contact-icon {
    width: 12px;
    height: 12px;
    fill: var(--brand-blue);
    flex: none;
  }
  .address {
    position: absolute;
    left: 33px;
    top: 428px;
    margin: 0;
    font-family: "Lato", sans-serif;
    font-style: normal;
    font-size: 14.5px;
    line-height: 17px;
    color: var(--ink);
  }
  .back-brand {
    position: absolute;
    left: 0;
    right: 0;
    top: 240px;
    text-align: center;
    font-family: "Lato", sans-serif;
    font-weight: 400;
    font-size: 24px;
    line-height: 28px;
    color: var(--light-gray);
    margin: 0;
    white-space: nowrap;
  }
  .slogan {
    position: absolute;
    left: 0;
    right: 0;
    top: 408px;
    margin: 0;
    text-align: center;
    font-family: "Montserrat", sans-serif;
    font-weight: 600;
    font-size: 17px;
    line-height: 22px;
    color: var(--paper);
    text-transform: uppercase;
  }
</style>
</head>
<body>
<main class="canvas">
  <section class="card card-front" aria-label="Business card front">
    <div class="brand">
      <span class="brand-square"></span>
      <p class="brand-name">Belford &amp; Company</p>
    </div>

    <div class="person">
      <h1 class="person-name">Marcus Reed</h1>
      <p class="person-title">Managing Director</p>
    </div>

    <ul class="contact-list">
      <li>
        <svg class="contact-icon" viewBox="0 0 12 12" aria-hidden="true"><path d="M1 4c0-2 2-3 5-3s5 1 5 3l-2 1-1-1H4L3 5z M2 11V7l2-2h4l2 2v4z"/></svg>
        212 300 4170
      </li>
      <li>
        <svg class="contact-icon" viewBox="0 0 12 12" aria-hidden="true"><path d="M3 0h6v12H3z M4 1.5v7.5h4V1.5z" fill-rule="evenodd"/></svg>
        917 620 3854
      </li>
      <li>
        <svg class="contact-icon" viewBox="0 0 12 12" aria-hidden="true"><path d="M3 0h6v3H3z M0 4h12v5h-2v3H2V9H0z M3 8v3h6V8z" fill-rule="evenodd"/></svg>
        212 300 4171
      </li>
      <li>
        <svg class="contact-icon" viewBox="0 0 12 12" aria-hidden="true"><path d="M0 2h12v8H0z M1 3l5 4 5-4z" fill-rule="evenodd"/></svg>
        mreed@belfordandcompany.example
      </li>
      <li>
        <svg class="contact-icon" viewBox="0 0 12 12" aria-hidden="true"><circle cx="6" cy="6" r="6"/><path d="M3 4h3v3H4z M7 7h2v2H7z" fill="#fff"/></svg>
        www.belfordandcompany.example
      </li>
    </ul>

    <address class="address">48 Harbor Street, Suite 900<br>Easton, NY 10027</address>
  </section>

  <section class="card card-back" aria-label="Business card back">
    <p class="back-brand">Belford &amp; Company</p>
    <p class="slogan">Careful Work,<br>Lasting Value</p>
  </section>
</main>
</body>
</html>
```